Ductless Mini Split Business Website

Amber Kite Services is looking to design an eye catching educational website about installing Ductless mini splits.

Similar to this company.
https://www.cedarcoolair.com/

```html
<!DOCTYPE html>
<html lang="en">
<head>
<meta charset="utf-8">
<title>Amber Kite Services – Ductless Experts</title>
<link href="https://fonts.googleapis.com/css2?family=Righteous&family=Montserrat:wght@400;600;700&family=Open+Sans:wght@400;600&family=Roboto+Condensed:wght@700&display=swap" rel="stylesheet">
<style>
:root{
  --yellow:#fcd21c;
  --yellow-deep:#f2c200;
  --black:#000;
  --card:#3a3a3a;
  --grey-text:#bdbdbd;
  --white:#fff;
}
*{box-sizing:border-box;margin:0;padding:0}
html,body{width:1200px;height:4494px;overflow:hidden}
body{position:relative;background:var(--black);color:var(--white);font-family:"Open Sans",sans-serif}
.abs{position:absolute}
.title{font-family:"Righteous",sans-serif;color:var(--yellow);text-align:center;width:1200px;font-size:44px;-webkit-text-stroke:1px #5a4700;letter-spacing:0.5px}
.btn{position:absolute;height:42px;border-radius:21px;background:var(--yellow);color:#111;font-family:"Montserrat",sans-serif;font-weight:600;font-size:16px;display:flex;align-items:center;padding-left:32px;text-transform:uppercase;white-space:nowrap}
.btn::after{content:"";position:absolute;right:-14px;top:6px;width:30px;height:30px;border-radius:50%;background:var(--yellow-deep);border:2px solid #111}

/* header */
.site-header{left:0;top:0;width:1200px;height:115px;background:var(--black);border-bottom:5px solid var(--yellow)}
.brand{left:148px;top:22px;font-family:"Montserrat",sans-serif;font-weight:700;color:var(--yellow);font-size:22px;line-height:1.15;white-space:nowrap}
.brand small{display:block;font-size:15px;letter-spacing:1px}
.brand-dot{left:112px;top:26px;width:28px;height:28px;border-radius:50%;background:var(--yellow)}
.call{right:146px;top:20px;font-family:"Montserrat",sans-serif;font-size:14px;font-weight:600;display:flex;align-items:center;gap:8px}
.call b{color:var(--yellow);font-size:18px}
.nav{right:143px;top:72px;display:flex;gap:28px;font-family:"Montserrat",sans-serif;font-weight:600;font-size:13.5px}
.nav a{color:var(--white);text-decoration:none;padding:6px 0}
.nav a.active{background:var(--yellow);color:#111;padding:6px 10px}

/* hero */
.hero{left:0;top:120px;width:1200px;height:740px;background:linear-gradient(180deg,#d9d6cf 0%,#c9c5bd 55%,#8d8a85 78%,#4f4d4a 100%)}
.hero-title{left:515px;top:300px;font-family:"Righteous",sans-serif;font-size:70px;line-height:80px;color:var(--yellow);-webkit-text-stroke:2px #111;white-space:nowrap}
.dots{left:560px;top:778px;display:flex;gap:8px}
.dots i{width:9px;height:9px;border-radius:50%;background:#fff}
.dots i.on{background:var(--yellow)}

/* dark backdrop */
.backdrop{left:0;top:860px;width:1200px;height:3330px;background:
 linear-gradient(180deg,#000 0%,#000 10%,#161a22 20%,#0d0f14 40%,#0a0b0e 48%,#000 52%,#14171d 62%,#000 70%,#151820 80%,#0b0c0f 92%,#000 100%)}
.lead{left:180px;top:1062px;width:840px;text-align:center;font-size:14.5px;line-height:33px;color:#e8e8e8}

/* hexagons */
.hex{position:absolute;width:279px;height:322px;clip-path:polygon(50% 0,100% 25%,100% 75%,50% 100%,0 75%,0 25%);display:flex;align-items:center;justify-content:center;text-align:center;padding-top:120px;font-family:"Roboto Condensed",sans-serif;font-weight:700;font-size:17px;color:var(--yellow);text-shadow:0 1px 3px #000;text-transform:uppercase;line-height:1.3}
.hex.photo{background:linear-gradient(160deg,#bfc4c8,#6d6f70 60%,#3d3d3d)}
.hex.feature{background:var(--yellow);color:#111;text-shadow:none}

/* why choose */
.why-band{left:0;top:2316px;width:1200px;height:474px}
.why-title{left:146px;top:2408px;font-family:"Righteous",sans-serif;font-size:43px;color:var(--yellow-deep);-webkit-text-stroke:1.5px #111;white-space:nowrap}
.why-item{left:146px;width:360px}
.why-item h3{margin-left:65px;font-family:"Montserrat",sans-serif;font-size:16px;color:#111}
.why-item p{margin-left:65px;margin-top:8px;font-size:13px;line-height:21px;color:#7a6200}
.why-icon{position:absolute;left:0;top:0;width:44px;height:40px}
.video{left:520px;top:2368px;width:553px;height:367px;background:#0a0a0a}
.video-shot{left:541px;top:2391px;width:514px;height:324px;background:linear-gradient(135deg,#9a9a92,#6a6b63 45%,#3c3d39)}

/* cards */
.card{position:absolute;top:3090px;width:290px;height:353px;background:var(--card)}
.card-shot{position:absolute;left:8px;top:7px;width:274px;height:163px;background:linear-gradient(180deg,#eef0f2,#c7cbd0)}
.card h3{position:absolute;left:19px;top:195px;font-family:"Montserrat",sans-serif;font-size:16px;font-weight:700}
.card p{position:absolute;left:19px;top:228px;width:240px;font-size:13px;line-height:21px;color:var(--grey-text)}
.card .outline{position:absolute;left:19px;top:297px;width:150px;height:36px;border:2px solid var(--yellow);border-radius:18px;color:var(--yellow);font-family:"Montserrat",sans-serif;font-weight:700;font-size:13px;display:flex;align-items:center;justify-content:center}

/* contact */
.fill-line{left:0;top:3696px;width:1200px;text-align:center;font-family:"Montserrat",sans-serif;font-weight:600;font-size:16px}
.fill-phone{left:0;top:3722px;width:1200px;text-align:center;font-family:"Montserrat",sans-serif;font-weight:700;font-size:24px;color:var(--yellow)}
.field{position:absolute;background:#fff;color:#777;font-size:11px;padding:8px 18px}

/* footer */
.foot-brand{left:148px;top:4290px;font-family:"Montserrat",sans-serif;font-weight:700;color:var(--yellow);font-size:30px;line-height:1.2;white-space:nowrap}
.foot-brand small{display:block;font-size:22px;letter-spacing:1.5px}
.foot-dot{left:104px;top:4296px;width:34px;height:34px;border-radius:50%;background:var(--yellow)}
.foot-nav{left:488px;top:4276px;font-family:"Montserrat",sans-serif;font-weight:600;font-size:15px;word-spacing:4px;white-space:nowrap}
.foot-copy{left:488px;top:4322px;font-size:12px;color:#ddd}
.social{left:488px;top:4366px;display:flex;gap:6px}
.social i{width:30px;height:30px;border-radius:50%;border:1.5px solid #fff}
.to-top{left:896px;top:4444px;width:159px;height:50px;background:var(--yellow);color:#111;font-family:"Montserrat",sans-serif;font-weight:600;font-size:15px;display:flex;align-items:center;justify-content:center}
</style>
</head>
<body>

<header class="abs site-header">
  <span class="abs brand-dot"></span>
  <div class="abs brand">Amber Kite Services<small>DUCTLESS EXPERTS</small></div>
  <div class="abs call">
    <svg width="32" height="32" viewBox="0 0 32 32"><circle cx="16" cy="16" r="14" fill="none" stroke="#fcd21c" stroke-width="2"/><path d="M11 9l3 0 1.5 4-2 1.5a9 9 0 0 0 4 4l1.5-2 4 1.5v3c0 1-1 1.5-2 1.5-6 0-12-6-12-12 0-1 .5-1.5 2-1.5z" fill="#fcd21c"/></svg>
    CALL <b>1 800 555 0142</b>
  </div>
  <nav class="abs nav"><a class="active">HOME</a><a>ABOUT US</a><a>SERVICES</a><a>NEWS</a><a>REVIEWS</a><a>CONTACT US</a></nav>
</header>

<section class="abs hero" role="img" aria-label="Woman relaxing on a grey sofa in a bright brick-walled living room under a wall-mounted ductless unit"></section>
<div class="abs hero-title">Amber Kite<br>Services</div>
<div class="abs dots"><i></i><i></i><i class="on"></i><i></i><i></i></div>

<div class="abs backdrop" role="img" aria-label="Dark night mountain landscape with forest and a road"></div>

<h2 class="abs title" style="top:966px">Welcome To Amber Kite Services</h2>
<p class="abs lead">Lorem ipsum dolor sit amet, consectetur adipiscing elit, sed do eiusmod tempor incididunt ut labore et dolore magna aliqua. Ut enim ad minim veniam, quis nostrud exercitation ullamco laboris nisi ut aliquip ex ea commodo consequat. Duis aute irure dolor in reprehenderit in voluptate velit esse cillum dolore eu fugiat nulla pariaturxcepteur sint occaecpidatat non proident, sunt in culpa qui officia deserunt mollit anim id est laborum</p>
<a class="btn" style="left:503px;top:1251px;width:178px">Read More</a>

<div class="hex photo" style="left:18px;top:1457px" role="img" aria-label="Technician servicing an indoor wall unit">Baseboard Heat<br>Replacement</div>
<div class="hex feature" style="left:314px;top:1457px">Whole House<br>Ductless</div>
<div class="hex photo" style="left:607px;top:1457px" role="img" aria-label="Worker in hard hat installing a unit">Ductless<br>Installation</div>
<div class="hex photo" style="left:902px;top:1457px" role="img" aria-label="Technician cleaning a coil with a sprayer">Ductless<br>Maintenance</div>
<div class="hex photo" style="left:164px;top:1714px" role="img" aria-label="Hands repairing wiring of an outdoor unit">Ductless Repairs</div>
<div class="hex photo" style="left:461px;top:1714px" role="img" aria-label="Wall unit parts and tools on a table">Ductless Warranty</div>
<div class="hex photo" style="left:757px;top:1714px" role="img" aria-label="Outdoor heat pump beside a house">Ductless Heat<br>Pump FAQ</div>

<a class="btn" style="left:470px;top:2100px;width:248px">View More Services</a>

<svg class="abs why-band" viewBox="0 0 1200 474" width="1200" height="474"><path d="M0 0 H560 L628 474 H0Z" fill="#fcd21c"/></svg>
<h2 class="abs why-title">Why Choose Us?</h2>
<div class="abs why-item" style="top:2514px">
  <svg class="why-icon" viewBox="0 0 44 40"><rect x="3" y="5" width="34" height="24" rx="2" fill="none" stroke="#111" stroke-width="2"/><line x1="9" y1="13" x2="30" y2="13" stroke="#111" stroke-width="2"/><line x1="9" y1="19" x2="24" y2="19" stroke="#111" stroke-width="2"/><circle cx="34" cy="30" r="6" fill="none" stroke="#111" stroke-width="2"/></svg>
  <h3>0% Financing for 60 months</h3>
  <p>Sed ut perspiciatis unde omnis iste natus error sit volcusantium</p>
</div>
<div class="abs why-item" style="top:2622px">
  <svg class="why-icon" viewBox="0 0 44 40"><circle cx="24" cy="14" r="11" fill="none" stroke="#111" stroke-width="2"/><text x="24" y="19" font-size="13" text-anchor="middle" fill="#111" font-family="sans-serif">$</text><path d="M2 32 Q12 26 20 30 L32 32" fill="none" stroke="#111" stroke-width="2"/></svg>
  <h3>365 Day, Money Back Guarantee</h3>
  <p>Sed ut perspiciatis unde omnis iste natus error sit volcusantium</p>
</div>
<div class="abs video"></div>
<div class="abs video-shot" role="img" aria-label="Technician testing the wiring of a heat pump with a multimeter"></div>
<svg class="abs" style="left:760px;top:2516px" width="76" height="76" viewBox="0 0 76 76"><circle cx="38" cy="38" r="35" fill="none" stroke="#fff" stroke-width="4"/><path d="M30 24 L54 38 30 52Z" fill="#fff"/></svg>

<h2 class="abs title" style="top:2968px">We Stand Behind Our Ductless Services</h2>
<article class="card" style="left:143px"><div class="card-shot" role="img" aria-label="Installer drilling above an indoor unit"></div><h3>Nemo enim ioluptatem</h3><p>Sed ut perspiciatis unde omnis iste natus error sit volcusantium</p><span class="outline">READ MORE</span></article>
<article class="card" style="left:455px"><div class="card-shot" role="img" aria-label="Worker on a ladder mounting outdoor units on a wall"></div><h3>Nemo enim ioluptatem</h3><p>Sed ut perspiciatis unde omnis iste natus error sit volcusantium</p><span class="outline">READ MORE</span></article>
<article class="card" style="left:767px"><div class="card-shot" role="img" aria-label="Technician beside an open indoor unit"></div><h3>Nemo enim ioluptatem</h3><p>Sed ut perspiciatis unde omnis iste natus error sit volcusantium</p><span class="outline">READ MORE</span></article>

<h2 class="abs title" style="top:3606px">Contact Us Today</h2>
<p class="abs fill-line">Fill Out the Form Below &nbsp;or Call us at</p>
<p class="abs fill-phone">1 800 555 0142</p>
<div class="field" style="left:293px;top:3802px;width:300px;height:32px">Your Name</div>
<div class="field" style="left:607px;top:3802px;width:298px;height:32px">Email Address</div>
<div class="field" style="left:293px;top:3847px;width:300px;height:32px">Phone</div>
<div class="field" style="left:607px;top:3847px;width:298px;height:32px">Address</div>
<div class="field" style="left:293px;top:3893px;width:612px;height:89px">Comments</div>
<a class="btn" style="left:483px;top:4034px;width:208px">Submit Message</a>

<footer>
  <span class="abs foot-dot"></span>
  <div class="abs foot-brand">Amber Kite Services<small>DUCTLESS EXPERTS</small></div>
  <div class="abs foot-nav">HOME &nbsp;/ &nbsp;ABOUT US &nbsp;/ &nbsp;SERVICES &nbsp;/ &nbsp;NEWS &nbsp;/ &nbsp;REVIEWS &nbsp;/ &nbsp;CONTACT US</div>
  <p class="abs foot-copy">© Copyright 2019 Amber Kite Services. All rights reserved.</p>
  <div class="abs social"><i></i><i></i><i></i><i></i></div>
  <a class="abs to-top">BACK TO TOP</a>
</footer>

</body>
</html>
```